Business Cards and Stationery- Lumen Quill Studio
Lumen Quill Studio
Business Cards and Stationery- Lumen Quill Studio - Miscellaneous
Creative Brief
Bright & Fun-filled
Marisol Quenby
Bramblewick, IL
lumen.quill.stdo@brightpost.test
lumen-quill-studio.test
I would like the business cards to just have the above web address and email. I would also like a 4X5 post card with this additional information: Facebook: facebook.com/groups/lumen.quill.studio Instagram: lumen.quill.studio Twitter: @LumenQuillStd Pinterest: pinterest.com/LumenQuillStd/
Not sure if I just want the logo, i'm open to anything

```html
<!DOCTYPE html>
<html lang="en">
<head>
<meta charset="utf-8">
<title>Lumen Quill Studio — Business Card</title>
<link rel="stylesheet" href="https://fonts.googleapis.com/css2?family=Montserrat:wght@500;600;700&display=swap">
<style>
  :root {
    --backdrop: #e9e6e1;
    --navy: #1a1a8c;
    --navy-deep: #14146e;
    --paper: #ffffff;
    --ink: #1a1a8c;
    --ink-soft: #4a4a6a;
    --on-navy: #ffffff;
  }
  html, body {
    margin: 0;
    padding: 0;
    width: 1200px;
    height: 904px;
    overflow: hidden;
    background: var(--backdrop);
    font-family: "Montserrat", Arial, sans-serif;
  }
  .canvas {
    position: relative;
    width: 1200px;
    height: 904px;
  }
  .card {
    position: absolute;
    width: 620px;
    height: 354px;
    box-shadow: 0 10px 24px rgba(0,0,0,0.18);
    overflow: hidden;
  }
  .card-front {
    left: 70px;
    top: 70px;
    background: linear-gradient(160deg, var(--navy) 0%, var(--navy-deep) 100%);
    color: var(--on-navy);
  }
  .front-name {
    position: absolute;
    left: 0;
    right: 0;
    top: 138px;
    text-align: center;
    font-weight: 600;
    font-size: 40px;
    letter-spacing: 0.5px;
  }
  .front-web {
    position: absolute;
    left: 0;
    right: 0;
    bottom: 34px;
    text-align: center;
    font-weight: 500;
    font-size: 15px;
    letter-spacing: 0.4px;
  }
  .card-back {
    left: 510px;
    top: 480px;
    background: var(--paper);
    color: var(--ink);
  }
  .back-name {
    position: absolute;
    left: 34px;
    top: 44px;
    font-weight: 600;
    font-size: 24px;
    color: var(--ink);
  }
  .contact {
    position: absolute;
    left: 300px;
    top: 168px;
  }
  .person {
    font-weight: 700;
    font-size: 19px;
    color: var(--ink);
    margin: 0 0 14px 0;
  }
  .contact-list {
    list-style: none;
    margin: 0;
    padding: 0;
  }
  .contact-list li {
    display: flex;
    align-items: center;
    gap: 10px;
    font-size: 13px;
    font-weight: 500;
    color: var(--ink-soft);
    line-height: 24px;
  }
  .contact-list svg {
    width: 14px;
    height: 14px;
    flex: none;
  }
</style>
</head>
<body>
<main class="canvas">
  <section class="card card-front" aria-label="Business card front">
    <div class="front-name">Lumen Quill Studio</div>
    <div class="front-web">www.lumen-quill-studio.test</div>
  </section>

  <section class="card card-back" aria-label="Business card back">
    <div class="back-name">Lumen Quill Studio</div>
    <div class="contact">
      <p class="person">Marisol Quenby</p>
      <ul class="contact-list">
        <li>
          <svg viewBox="0 0 24 24" aria-hidden="true"><path fill="var(--ink)" d="M12 2a7 7 0 0 0-7 7c0 5 7 13 7 13s7-8 7-13a7 7 0 0 0-7-7zm0 9.5A2.5 2.5 0 1 1 12 6.5a2.5 2.5 0 0 1 0 5z"/></svg>
          Bramblewick, IL
        </li>
        <li>
          <svg viewBox="0 0 24 24" aria-hidden="true"><rect x="2" y="5" width="20" height="14" rx="2" fill="var(--ink)"/><path d="M3 6l9 7 9-7" fill="none" stroke="#fff" stroke-width="1.8"/></svg>
          lumen.quill.stdo@brightpost.test
        </li>
        <li>
          <svg viewBox="0 0 24 24" aria-hidden="true"><circle cx="12" cy="12" r="10" fill="var(--ink)"/><path d="M2 12h20M12 2c3 3 3 17 0 20M12 2c-3 3-3 17 0 20" fill="none" stroke="#fff" stroke-width="1.4"/></svg>
          www.lumen-quill-studio.test
        </li>
      </ul>
    </div>
  </section>
</main>
</body>
</html>
```